Patent Law

Need to develop a home page for a patent lawyer.

Colors should go with logo, blues...

Company Name- Corvel Tindry, PLLC

Company Overview-

I am an Intellectual Property Lawyer and focus on patents, copyrights, trademarks, & trade secrets. I work with small businesses and start ups in the chemical and biotech industries.

Why Us-

I am small firm that can provide large-firm service at a reasonable price. I also can charge flat-fees for entreprenuers in certain practice areas.

Services-
Intellectual Property
Patents
Copyrights
Trademarks
Trade secrets
Healthcare Compliance
Elder law
Wills
Trusts

Website we like-
http://www.quarnlowtide.example/ - within industry!!
http://www.vopperhask.example/
http://dulbrickovan.example/
http://thefernwoldguides.example/

Target Market(s)

My customers will be small business, specifically small start-up companies in the chemical and biotech arena.

Industry/Entity Type

Trade

Requirements
Must have
• Colors should go with logo, blues...

```html
<!DOCTYPE html>
<html lang="en">
<head>
<meta charset="utf-8">
<title>Corvel Tindry, PLLC</title>
<link href="https://fonts.googleapis.com/css2?family=Open+Sans:wght@400;600;700&display=swap" rel="stylesheet">
<style>
:root{
  --brand-blue:#0090d9;
  --slate:#4a5862;
  --ink:#3d4a55;
  --muted:#777d82;
  --white:#ffffff;
  --hero-warm:#8a5a40;
  --hero-deep:#5e4238;
}
*{margin:0;padding:0;box-sizing:border-box}
html,body{width:1200px;height:712px;overflow:hidden;background:var(--white);font-family:"Open Sans",Arial,sans-serif}
.page{position:relative;width:1200px;height:712px}
.top-rule{position:absolute;left:0;top:0;width:1200px;height:4px;background:var(--brand-blue)}
.bottom-rule{position:absolute;left:0;top:707px;width:1200px;height:5px;background:var(--brand-blue)}

.brand{position:absolute;left:161px;top:24px;display:flex;flex-direction:column;align-items:center;width:150px}
.brand-mark{width:44px;height:44px;border-radius:50%;background:var(--brand-blue);margin-bottom:12px}
.brand-name{font-size:14px;font-weight:600;color:var(--ink);letter-spacing:.5px;white-space:nowrap;text-transform:uppercase}

.contact-strip{position:absolute;top:22px;left:829px;display:flex;align-items:center;font-size:13px;color:var(--muted)}
.contact-icon{width:24px;height:24px;border:1px solid var(--ink);display:flex;align-items:center;justify-content:center;margin-right:11px}
.contact-item{display:flex;align-items:center;margin-right:18px}

.main-nav{position:absolute;left:482px;top:63px;height:44px;display:flex;background:var(--brand-blue)}
.main-nav a{display:flex;align-items:center;justify-content:center;height:44px;color:var(--white);font-weight:700;font-size:13px;text-decoration:none;text-transform:uppercase}
.main-nav a.active{background:var(--slate)}

.hero{position:absolute;left:0;top:129px;width:1200px;height:464px;
  background:linear-gradient(120deg,var(--hero-warm) 0%,#8f6450 55%,var(--hero-deep) 100%)}

.why-us{position:absolute;left:161px;top:298px;width:288px;height:295px;background:var(--slate);color:var(--white)}
.why-us h2{text-align:center;font-size:26px;font-weight:700;margin-top:28px}
.why-us p{margin:12px 0 0 34px;width:226px;font-size:12px;line-height:19px}
.more-btn{position:absolute;left:102px;top:232px;width:84px;height:34px;border:1px solid var(--white);display:flex;align-items:center;justify-content:center;font-size:12px;font-weight:700;color:var(--white);text-decoration:none}

.cta{position:absolute;top:530px;width:288px;height:63px;background:var(--brand-blue);color:var(--white);display:flex;align-items:center;justify-content:center;font-size:27px;font-weight:700;text-decoration:none;text-transform:uppercase}
.cta::before{content:"";position:absolute;top:-13px;left:131px;border-left:13px solid transparent;border-right:13px solid transparent;border-bottom:13px solid var(--brand-blue)}
.cta-services{left:456px}
.cta-contact{left:751px}

.footer-nav{position:absolute;left:160px;top:630px;display:flex;font-size:12px;color:var(--muted)}
.footer-nav a{color:var(--muted);text-decoration:none}
.footer-nav .sep{width:1px;height:12px;background:#c5c8cb;margin:3px 12px 0}
.copyright{position:absolute;left:160px;top:654px;font-size:12px;color:var(--muted)}
.social{position:absolute;left:956px;top:631px;display:flex;gap:15px}
.social span{width:17px;height:17px;border-radius:50%;background:#80868b}
</style>
</head>
<body>
<div class="page">
  <div class="top-rule"></div>

  <header>
    <div class="brand">
      <span class="brand-mark"></span>
      <span class="brand-name">Corvel Tindry, PLLC</span>
    </div>

    <div class="contact-strip">
      <div class="contact-item">
        <span class="contact-icon">
          <svg width="12" height="12" viewBox="0 0 24 24"><path fill="#0090d9" d="M6.6 10.8a15.1 15.1 0 0 0 6.6 6.6l2.2-2.2c.3-.3.7-.4 1-.2 1.1.4 2.3.6 3.6.6.6 0 1 .4 1 1V20c0 .6-.4 1-1 1A17 17 0 0 1 3 4c0-.6.4-1 1-1h3.5c.6 0 1 .4 1 1 0 1.3.2 2.5.6 3.6.1.3 0 .7-.2 1z"/></svg>
        </span>
        +97 990-555-218
      </div>
      <div class="contact-item">
        <span class="contact-icon">
          <svg width="12" height="14" viewBox="0 0 24 28"><path fill="#0090d9" d="M12 0a9 9 0 0 0-9 9c0 6.8 9 19 9 19s9-12.2 9-19a9 9 0 0 0-9-9zm0 12.5A3.5 3.5 0 1 1 12 5.5a3.5 3.5 0 0 1 0 7z"/></svg>
        </span>
        Map
      </div>
    </div>

    <nav class="main-nav">
      <a class="active" href="#" style="width:78px">Home</a>
      <a href="#" style="width:97px">About us</a>
      <a href="#" style="width:91px">Services</a>
      <a href="#" style="width:101px">Practices</a>
      <a href="#" style="width:70px">News</a>
      <a href="#" style="width:120px">Contact us</a>
    </nav>
  </header>

  <section class="hero" role="img" aria-label="Photo of bound law case volumes on a wooden shelf with reading glasses in the foreground"></section>

  <section class="why-us">
    <h2>WHY US</h2>
    <p>Lorem Ipsum is simply dummy text of the printing and typesetting industry. Lorem Ipsum has been the industry's standard dummy text ever since the 1500s, when an unknown printer took a galley of type and scrambled it to make a type specimen book.</p>
    <a class="more-btn" href="#">MORE</a>
  </section>

  <a class="cta cta-services" href="#">Services</a>
  <a class="cta cta-contact" href="#">Contact us</a>

  <footer>
    <div class="footer-nav">
      <a href="#">Home</a><span class="sep"></span>
      <a href="#">About Us</a><span class="sep"></span>
      <a href="#">Services</a><span class="sep"></span>
      <a href="#">Practices</a><span class="sep"></span>
      <a href="#">News</a><span class="sep"></span>
      <a href="#">Contact us</a>
    </div>
    <div class="copyright">Copyright © 2014 Corvel tindry pllc.</div>
    <div class="social"><span></span><span></span><span></span></div>
  </footer>

  <div class="bottom-rule"></div>
</div>
</body>
</html>
```